business card for LWR pty ltd

We require a business card that stands out . I have included our company flyer and would like the services listed to be put on the card so when we Give out the cards to customers they have an idea of services we provide. need the winning design to be in editable photo shop format, editable iMac pages format or editable windows publisher format, so that I can enter in names, email addresses, phone numbers etc myself. I have included a pdf documents of info / items needed on the card to use as reference please.
Updates

need more submissions

Need extra days to review

Sick

Target Market(s)

new customers

Contact Information for Business Card

details are on attached business card requirements file

Requirements
Must have
• I have attached a list of must haves

```html
<!DOCTYPE html>
<html lang="en">
<head>
<meta charset="utf-8">
<title>LWR pty ltd business card</title>
<link rel="stylesheet" href="https://fonts.googleapis.com/css2?family=Michroma&family=Cabin+Condensed:wght@500;600&family=Open+Sans:wght@400;600&display=swap">
<style>
  :root {
    --page: #d9d9d9;
    --card-dark: #111214;
    --card-dark-edge: #1d1f22;
    --card-light: #ffffff;
    --metal: #8a8d92;
    --metal-light: #c9ccd0;
    --ink: #3a3b3d;
    --ink-soft: #5c5e61;
    --service-text: #f2f2f2;
    --truck-sky: #2b2e33;
    --truck-tone: #8c7a5c;
  }
  * { box-sizing: border-box; margin: 0; padding: 0; }
  html, body { width: 1200px; height: 675px; overflow: hidden; }
  body {
    background: var(--page);
    display: flex;
    align-items: center;
    justify-content: center;
    gap: 60px;
  }
  .card {
    position: relative;
    width: 520px;
    height: 297px;
    border-radius: 16px;
    overflow: hidden;
    box-shadow: 0 10px 24px rgba(0,0,0,0.22);
  }

  /* Back side: services */
  .card--services {
    background: radial-gradient(ellipse at 45% 15%, var(--card-dark-edge), var(--card-dark) 70%);
  }
  .card--services .brand-mark {
    position: absolute;
    left: 118px;
    top: 36px;
    font-family: "Michroma", sans-serif;
    font-size: 58px;
    letter-spacing: 4px;
    color: var(--metal-light);
    line-height: 1;
  }
  .truck-photo {
    position: absolute;
    left: 22px;
    top: 122px;
    width: 300px;
    height: 110px;
    border-radius: 6px;
    background: linear-gradient(180deg, var(--truck-sky) 0%, #4a4d52 45%, var(--truck-tone) 100%);
  }
  .services {
    position: absolute;
    left: 330px;
    top: 80px;
    width: 180px;
    font-family: "Cabin Condensed", sans-serif;
    font-weight: 600;
    font-style: italic;
    color: var(--service-text);
    font-size: 12.5px;
    line-height: 1.32;
  }
  .services__title {
    font-size: 13px;
    margin-bottom: 2px;
    letter-spacing: 0.3px;
  }
  .services__list { list-style: none; }
  .services__list li::before { content: "• "; }
  .services__list .continued::before { content: ""; }

  /* Front side: contact */
  .card--contact { background: var(--card-light); }
  .card--contact .brand-mark {
    position: absolute;
    left: 40px;
    top: 44px;
    font-family: "Michroma", sans-serif;
    font-size: 64px;
    letter-spacing: 4px;
    color: var(--metal);
    line-height: 1;
  }
  .person {
    position: absolute;
    right: 36px;
    top: 140px;
    text-align: right;
    font-family: "Michroma", sans-serif;
    color: var(--ink);
  }
  .person__name { font-size: 17px; letter-spacing: 5px; }
  .person__role { font-size: 8.5px; letter-spacing: 3px; margin-top: 8px; }
  .contact-list {
    position: absolute;
    left: 40px;
    top: 188px;
    list-style: none;
    font-family: "Open Sans", sans-serif;
    font-size: 11px;
    color: var(--ink-soft);
    line-height: 1.55;
  }
  .contact-list li { display: flex; align-items: flex-start; gap: 8px; }
  .contact-list .icon { width: 11px; height: 11px; margin-top: 3px; flex: none; fill: var(--ink); }
  .contact-list .no-icon { padding-left: 19px; }
  .contact-list .company { font-weight: 600; color: var(--ink); }
</style>
</head>
<body>

  <section class="card card--services">
    <div class="brand-mark">LWR</div>
    <div class="truck-photo" role="img" aria-label="Photo of a road train truck hauling tanker trailers"></div>
    <div class="services">
      <p class="services__title">OUR SERVICES</p>
      <ul class="services__list">
        <li>Over Size Loads / Hot Shot Loads</li>
        <li>Heavy Vehicle Recovery Services</li>
        <li>Potable Water Deliveries</li>
        <li>Road Building / Maintenance</li>
        <li>Earthworks</li>
        <li>Sand &amp; Metal Supply &amp; Cartage</li>
        <li>Road Train Tippers</li>
        <li>Road Train Tankers</li>
        <li>Road Train Flat Tops</li>
        <li>Drop Deck Trailers</li>
        <li>Mine Site Accredited Equipment</li>
        <li class="continued">&amp; Operator</li>
      </ul>
    </div>
  </section>

  <section class="card card--contact">
    <div class="brand-mark">LWR</div>
    <div class="person">
      <p class="person__name">DANIEL HART</p>
      <p class="person__role">DIRECTOR</p>
    </div>
    <ul class="contact-list">
      <li>
        <svg class="icon" viewBox="0 0 12 12" aria-hidden="true"><path d="M6 0a4 4 0 0 0-4 4c0 3 4 8 4 8s4-5 4-8a4 4 0 0 0-4-4zm0 5.6A1.6 1.6 0 1 1 6 2.4a1.6 1.6 0 0 1 0 3.2z"/></svg>
        <span class="company">LWR PTY LTD</span>
      </li>
      <li class="no-icon">Lot 444 example address Australia</li>
      <li>
        <svg class="icon" viewBox="0 0 12 12" aria-hidden="true"><path d="M0 2h12v8H0z M1 3l5 3.5L11 3" stroke="#fff" stroke-width="1"/></svg>
        <span>email@lwrservices.com.au</span>
      </li>
      <li>
        <svg class="icon" viewBox="0 0 12 12" aria-hidden="true"><path d="M3 0l2 3-1.3 1.3a7 7 0 0 0 4 4L9 7l3 2-1.5 2.5C5 11 1 7 .5 1.5z"/></svg>
        <span>000 444 000</span>
      </li>
      <li>
        <svg class="icon" viewBox="0 0 12 12" aria-hidden="true"><circle cx="6" cy="6" r="5.5"/><path d="M.5 6h11M6 .5c-3 3-3 8 0 11M6 .5c3 3 3 8 0 11" stroke="#fff" stroke-width="0.8" fill="none"/></svg>
        <span>www.lwrservices.com.au</span>
      </li>
    </ul>
  </section>

</body>
</html>
```